Building company business card

Design and print business cards for BRENTHOLM PTY LTD.
A residantial homes building company.
Mark Lantern already designed the company Logo.

```html
<!DOCTYPE html>
<html lang="en">
<head>
<meta charset="utf-8">
<title>BRENTHOLM PTY LTD – Business Card</title>
<link href="https://fonts.googleapis.com/css2?family=Montserrat:wght@300;400;800&family=Oswald:wght@700&display=swap" rel="stylesheet">
<style>
  :root {
    --navy: #232a66;
    --gold: #d39a2e;
    --gold-deep: #b07b1c;
    --cream: #efe6d2;
    --white: #ffffff;
    --grey-text: #8a8a8a;
    --page: #e9e7e3;
  }
  html, body {
    margin: 0;
    padding: 0;
    width: 1200px;
    height: 900px;
    overflow: hidden;
    background: var(--page);
  }
  .canvas {
    position: relative;
    width: 1200px;
    height: 900px;
  }
  .card {
    position: absolute;
    width: 600px;
    height: 343px;
    overflow: hidden;
    box-shadow: 0 10px 30px rgba(0,0,0,0.18);
  }

  /* Front */
  .card-front {
    left: 80px;
    top: 80px;
    background: var(--navy);
  }
  .front-wordmark {
    position: absolute;
    left: 64px;
    top: 0;
    height: 343px;
    display: flex;
    align-items: center;
    margin: 0;
    font-family: "Oswald", sans-serif;
    font-weight: 700;
    font-size: 64px;
    line-height: 1;
    letter-spacing: 0.5px;
    color: var(--white);
    z-index: 1;
  }
  .front-stripe-field {
    position: absolute;
    right: 0;
    top: 0;
    width: 170px;
    height: 343px;
    background: linear-gradient(120deg, var(--navy) 0%, var(--gold-deep) 55%, var(--gold) 100%);
  }

  /* Back */
  .card-back {
    left: 520px;
    top: 477px;
    background: linear-gradient(110deg, #f4f4f4 0%, var(--white) 60%, #f6f6f6 100%);
  }
  .back-stripe-field {
    position: absolute;
    left: 0;
    top: 150px;
    width: 330px;
    height: 193px;
    background: linear-gradient(90deg, var(--cream) 0%, rgba(239,230,210,0.35) 70%, rgba(239,230,210,0) 100%);
  }
  .brand-lockup {
    position: absolute;
    right: 36px;
    top: 40px;
    display: flex;
    align-items: center;
    gap: 12px;
  }
  .brand-square {
    width: 26px;
    height: 26px;
    background: var(--gold);
  }
  .brand-name {
    font-family: "Oswald", sans-serif;
    font-weight: 700;
    font-size: 44px;
    line-height: 1;
    color: var(--navy);
  }
  .registration {
    position: absolute;
    right: 36px;
    top: 160px;
    text-align: right;
    font-family: "Montserrat", sans-serif;
    font-weight: 400;
    font-size: 13px;
    line-height: 1.45;
    color: var(--navy);
  }
  .person {
    position: absolute;
    left: 40px;
    top: 168px;
    font-family: "Montserrat", sans-serif;
  }
  .person-name {
    margin: 0;
    font-weight: 800;
    font-size: 15px;
    color: var(--navy);
    letter-spacing: 0.3px;
  }
  .person-role {
    margin: 2px 0 0;
    font-weight: 400;
    font-size: 13px;
    color: var(--grey-text);
  }
  .contacts {
    position: absolute;
    left: 40px;
    top: 228px;
    margin: 0;
    padding: 0;
    list-style: none;
    font-family: "Montserrat", sans-serif;
    font-weight: 300;
    font-size: 13px;
    color: #4a4a4a;
  }
  .contacts li {
    display: flex;
    align-items: center;
    gap: 8px;
    height: 19px;
  }
  .contacts svg {
    width: 12px;
    height: 12px;
    fill: none;
    stroke: var(--navy);
    stroke-width: 1.6;
  }
  .contacts svg .solid { fill: var(--navy); stroke: none; }
</style>
</head>
<body>
<main class="canvas">

  <section class="card card-front" aria-label="Card front">
    <div class="front-stripe-field" role="img" aria-label="Gold diagonal stripe decoration on navy"></div>
    <h1 class="front-wordmark">BRENTHOLM</h1>
  </section>

  <section class="card card-back" aria-label="Card back">
    <div class="back-stripe-field" role="img" aria-label="Faint cream stripe decoration"></div>

    <div class="brand-lockup">
      <span class="brand-square"></span>
      <span class="brand-name">BRENTHOLM</span>
    </div>

    <div class="registration">
      ABN - 48 210 395 766<br>
      CDB- U 51846
    </div>

    <div class="person">
      <p class="person-name">DORIAN (Dory) FELLOWS</p>
      <p class="person-role">Director</p>
    </div>

    <ul class="contacts">
      <li>
        <svg viewBox="0 0 12 12"><rect x="3" y="1" width="6" height="10" rx="1"/></svg>
        0431 582 907
      </li>
      <li>
        <svg viewBox="0 0 12 12"><rect x="3" y="1" width="6" height="10" rx="1"/></svg>
        0462 318 540
      </li>
      <li>
        <svg viewBox="0 0 12 12"><path class="solid" d="M1 5 Q6 1 11 5 L10 6.5 L8 5.5 L8 4.5 Q6 3.8 4 4.5 L4 5.5 L2 6.5 Z"/><rect class="solid" x="3" y="7" width="6" height="4" rx="0.5"/></svg>
        0431 582 907
      </li>
      <li>
        <svg viewBox="0 0 12 12"><rect x="1.5" y="3" width="9" height="7"/><path d="M1.5 3 L6 7 L10.5 3"/></svg>
        dfw@brentholm-pl.com
      </li>
      <li>
        <svg viewBox="0 0 12 12"><path class="solid" d="M6 11.5 L2.5 6 A3.5 3.5 0 1 1 9.5 6 Z"/><circle cx="6" cy="4.6" r="1.3" fill="#fff" stroke="none"/></svg>
        PO Box 482, Fernvale East Vic 3920
      </li>
    </ul>
  </section>

</main>
</body>
</html>
```